Business Card for Willowcrest Terrain Advisors

We need a business card for Willowcrest Terrain Advisors. The company website address is provided below. The company logo is attached. We provide specialized permafrost services to the mining, transportation, and oil & gas industries. The card should be prepared for:
Dominic Halloway, PhD.
Willowcrest Terrain Advisors
PO Box 418529
Birch Hollow, Alaska 99612
Direct: +1-907-555-2964
Email: dhalloway@terrainadvisors-example.com
Website: www.willowcrestterrainadvisors-example.com

```html
<!DOCTYPE html>
<html lang="en">
<head>
<meta charset="utf-8">
<title>Willowcrest Terrain Advisors – Business Card</title>
<link href="https://fonts.googleapis.com/css2?family=Montserrat:wght@400;600;700&display=swap" rel="stylesheet">
<style>
  :root {
    --page: #ecebe8;
    --card: #ffffff;
    --ink: #16191e;
    --band-dark: #2c2d30;
    --band-light: #8e8f91;
    --rule: #1d1f23;
  }
  * { margin: 0; padding: 0; box-sizing: border-box; }
  html, body { width: 900px; height: 1200px; overflow: hidden; }
  body {
    background: var(--page);
    font-family: "Montserrat", Arial, sans-serif;
    color: var(--ink);
    position: relative;
  }
  .card {
    position: absolute;
    left: 80px;
    width: 740px;
    height: 440px;
    background: var(--card);
    border-radius: 40px;
    overflow: hidden;
    box-shadow: 0 6px 14px rgba(0,0,0,.18);
  }
  .card--front { top: 132px; }
  .card--back { top: 640px; }

  .wordmark {
    position: absolute;
    font-weight: 600;
    color: var(--ink);
    text-transform: uppercase;
    line-height: 1;
  }
  .wordmark span { display: block; }
  .card--front .wordmark {
    right: 53px;
    top: 58px;
    text-align: center;
  }
  .card--front .wordmark .main { font-size: 38px; letter-spacing: 3px; }
  .card--front .wordmark .sub { font-size: 14.5px; letter-spacing: 4.6px; margin-top: 8px; }

  .card--back .wordmark {
    left: 0; right: 0;
    top: 172px;
    text-align: center;
  }
  .card--back .wordmark .main { font-size: 62px; letter-spacing: 4px; }
  .card--back .wordmark .sub { font-size: 21px; letter-spacing: 7px; margin-top: 14px; }

  .person { position: absolute; left: 38px; top: 266px; }
  .person__name { font-size: 26px; font-weight: 700; letter-spacing: -.2px; }
  .person__role { font-size: 16px; font-weight: 400; margin-top: 3px; }

  .divider {
    position: absolute;
    left: 38px; top: 327px;
    width: 670px; height: 1.5px;
    background: var(--rule);
  }

  .contacts {
    position: absolute;
    left: 38px; top: 343px;
    list-style: none;
    font-size: 16px;
    line-height: 22px;
  }
  .contacts li { display: flex; align-items: center; gap: 12px; }
  .contacts svg { width: 14px; height: 14px; fill: var(--ink); flex: none; }

  .address {
    position: absolute;
    left: 503px; top: 365px;
    font-size: 16px;
    line-height: 20px;
    font-style: normal;
  }

  .band { position: absolute; left: 0; bottom: 0; width: 100%; height: 16px; }
</style>
</head>
<body>

<section class="card card--front" aria-label="Business card front">
  <div class="wordmark">
    <span class="main">Willowcrest</span>
    <span class="sub">Terrain Advisors</span>
  </div>

  <div class="person">
    <div class="person__name">Dominic Halloway, PhD.</div>
    <div class="person__role">CEO &amp; Founder</div>
  </div>

  <div class="divider"></div>

  <ul class="contacts">
    <li>
      <svg viewBox="0 0 16 16" aria-hidden="true"><path d="M2 5c0-2 3-3 6-3s6 1 6 3v1h-3V5H5v1H2zM4 7h8l2 6H2z M8 8.5a2 2 0 1 0 .01 0z"/></svg>
      +1-907-555-2964
    </li>
    <li>
      <svg viewBox="0 0 16 16" aria-hidden="true"><path d="M1 3h14v10H1z" fill="none"/><path d="M1 3h14v1.5L8 9 1 4.5zM1 6l7 4.5L15 6v7H1z"/></svg>
      dhalloway@terrainadvisors-example.com
    </li>
    <li>
      <svg viewBox="0 0 16 16" aria-hidden="true"><circle cx="8" cy="8" r="7"/><path d="M5 4c1 1 2 1 2 3s-2 1-2 3l1 2-3-1-1-4zM10 3c1 1 0 2 1 3s2 0 2 2-2 3-3 4l-1-3 1-2-1-2z" fill="#fff"/></svg>
      www.willowcrestterrainadvisors-example.com
    </li>
  </ul>

  <address class="address">
    PO Box 418529<br>
    Birch Hollow, Alaska 99612
  </address>

  <svg class="band" viewBox="0 0 740 16" preserveAspectRatio="none" aria-hidden="true">
    <polygon points="0,0 496,0 486,16 0,16" fill="var(--band-dark)"/>
    <polygon points="500,0 740,0 740,16 490,16" fill="var(--band-light)"/>
  </svg>
</section>

<section class="card card--back" aria-label="Business card back">
  <div class="wordmark">
    <span class="main">Willowcrest</span>
    <span class="sub">Terrain Advisors</span>
  </div>
  <svg class="band" viewBox="0 0 740 16" preserveAspectRatio="none" aria-hidden="true">
    <rect width="740" height="16" fill="var(--band-dark)"/>
  </svg>
</section>

</body>
</html>
```